Magnetic Business Card Design. One sided

Not happy yet with a design yet currently winning so far are the designs 5162585 5135573 5132280

Logo
unmatched Quality through traditional friendly service" sound like a good line. Blockages, Hot water units & all plumbing services.
7days,
free quote: 0467 215 340
Maybe put on it: Qualified, Licensed
www.brightflowplumbing.com.au

Make word as big so it is clearly able to be read

BrightFlow Plumbing PTY LTD, target market is the middle aged mostly woman professional that owns a house and would rather pay a professional to do the job rather then a handyman.
We are a plumbing company based in Melbourne small and family owned with a focus on service to our customers.

I am after a design that is clean, professional and appealing to the eye which fits with the visual appearance of my web site and logo.

Our most profitable jobs are blockages and hot water units. however we do all types of plumbing. Maybe a point to make on the cards not sure tho.

I have included our previous magnet that i had designed with a pixel press template. if you can improve what we say to get new customers or totally change what is on the magnet. that would be fantastic.

I will also include other marketing material i have previously used

"unmatched Quality Through traditional friendly service" Could be a good catch line

These magnets are dropped into thousands of letter boxes and hopefully will find there way onto new clients fridges. Fridges in million dollar plus houses.

I really look forward to seeing your design. Thank you

Industry/Entity Type

Marketing

Contact Information for Business Card

Number: 0467 215 340
Web site: www.Brightflowplumbing.com.au

```html
<!DOCTYPE html>
<html lang="en">
<head>
<meta charset="utf-8">
<title>BrightFlow Plumbing – Magnet Card</title>
<link rel="stylesheet" href="https://fonts.googleapis.com/css2?family=Anton&family=Open+Sans:wght@400;600;700&family=Roboto+Condensed:wght@400;700&display=swap">
<style>
  :root {
    --navy: #121a44;
    --blue: #1b4fa0;
    --ink: #111111;
    --silver-light: #f7f8fa;
    --silver-mid: #d9dde3;
    --white: #ffffff;
    --black: #000000;
  }
  html, body {
    margin: 0;
    padding: 0;
    width: 1200px;
    height: 740px;
    overflow: hidden;
    background: var(--white);
  }
  .card {
    position: relative;
    width: 1200px;
    height: 740px;
    overflow: hidden;
    background: linear-gradient(180deg, var(--silver-mid) 0%, var(--silver-light) 42%, var(--silver-mid) 100%);
    font-family: "Open Sans", Arial, sans-serif;
  }
  .brand {
    position: absolute;
    left: 60px;
    top: 40px;
    width: 760px;
    text-align: center;
  }
  .brand__since {
    margin: 0;
    font-size: 28px;
    font-weight: 700;
    color: var(--blue);
    line-height: 1;
  }
  .brand__name {
    margin: 10px 0 0;
    font-family: "Open Sans", Arial, sans-serif;
    font-weight: 700;
    color: var(--navy);
    font-size: 104px;
    line-height: 1.02;
    letter-spacing: -1px;
  }
  .brand__name span { display: block; }
  .brand__name .brand__sub {
    font-size: 64px;
    letter-spacing: 14px;
  }
  .hours {
    position: absolute;
    left: 868px;
    top: 100px;
    width: 300px;
    text-align: center;
    color: var(--ink);
  }
  .hours__days {
    display: flex;
    align-items: center;
    justify-content: center;
    gap: 8px;
    font-size: 50px;
    font-weight: 700;
    color: var(--blue);
    line-height: 1;
  }
  .hours__line {
    font-size: 46px;
    line-height: 60px;
  }
  .tagline {
    position: absolute;
    left: 0;
    width: 1200px;
    top: 338px;
    margin: 0;
    text-align: center;
    font-family: "Anton", Impact, sans-serif;
    font-size: 51px;
    line-height: 1.2;
    color: var(--ink);
    letter-spacing: 0.2px;
  }
  .services {
    position: absolute;
    left: 0;
    width: 1200px;
    top: 416px;
    margin: 0;
    text-align: center;
    font-size: 44px;
    color: var(--ink);
    line-height: 1.2;
  }
  .credentials {
    position: absolute;
    left: 72px;
    top: 518px;
    display: flex;
    align-items: center;
    gap: 18px;
  }
  .credentials__text {
    font-size: 28px;
    font-weight: 600;
    letter-spacing: 4px;
    line-height: 1.5;
    text-align: center;
    color: var(--ink);
  }
  .quote-band {
    position: absolute;
    left: 392px;
    top: 503px;
    width: 808px;
    height: 110px;
  }
  .quote-band__text {
    position: absolute;
    left: 45px;
    top: 0;
    height: 110px;
    display: flex;
    align-items: center;
    gap: 14px;
    color: var(--white);
    font-family: "Roboto Condensed", Arial, sans-serif;
    font-size: 58px;
    white-space: nowrap;
  }
  .quote-band__phone { font-weight: 700; font-size: 64px; }
  .web-bar {
    position: absolute;
    left: 0;
    top: 612px;
    width: 1200px;
    height: 128px;
    background: var(--black);
    color: var(--white);
    display: flex;
    align-items: center;
    justify-content: center;
    font-size: 62px;
    letter-spacing: 0.5px;
  }
  .web-bar strong { font-weight: 700; }
</style>
</head>
<body>
<main class="card">
  <header class="brand">
    <p class="brand__since">Since 1980</p>
    <h1 class="brand__name"><span>BrightFlow</span><span class="brand__sub">PLUMBING</span></h1>
  </header>

  <section class="hours">
    <div class="hours__days">
      <svg width="58" height="50" viewBox="0 0 58 50" aria-hidden="true">
        <circle cx="34" cy="22" r="18" fill="none" stroke="#121a44" stroke-width="4"/>
        <path d="M34 12 V22 L42 28" fill="none" stroke="#121a44" stroke-width="4" stroke-linecap="round"/>
        <rect x="2" y="28" width="26" height="14" rx="2" fill="#121a44"/>
        <circle cx="9" cy="44" r="4" fill="#121a44"/>
        <circle cx="23" cy="44" r="4" fill="#121a44"/>
      </svg>
      <span>7 DAYS</span>
    </div>
    <div class="hours__line">affordable</div>
    <div class="hours__line">&amp; reliable</div>
  </section>

  <p class="tagline">UNMATCHED QUALITY THROUGH TRADITION FRIENDLY SERVICE</p>
  <p class="services">Blockages, hot water units &amp; all plumbing services.</p>

  <div class="credentials">
    <svg width="52" height="76" viewBox="0 0 52 76" aria-hidden="true">
      <path d="M12 40 L4 72 L16 64 L22 76 L26 48 Z" fill="#111"/>
      <path d="M40 40 L48 72 L36 64 L30 76 L26 48 Z" fill="#111"/>
      <circle cx="26" cy="26" r="24" fill="#111"/>
      <circle cx="26" cy="26" r="16" fill="none" stroke="#fff" stroke-width="3"/>
    </svg>
    <div class="credentials__text">QUALIFIED<br>LICENSED</div>
  </div>

  <div class="quote-band">
    <svg width="808" height="110" viewBox="0 0 808 110" aria-hidden="true">
      <path d="M38 0 H808 V110 H0 L22 14 Q26 0 38 0 Z" fill="#1b4fa0"/>
    </svg>
    <div class="quote-band__text">
      <span>Free Quote</span>
      <svg width="34" height="44" viewBox="0 0 34 44" aria-hidden="true">
        <path d="M8 2 L15 12 L10 18 Q13 27 20 32 L26 27 L33 36 L26 42 Q12 40 4 24 Q0 12 8 2 Z" fill="#fff"/>
      </svg>
      <span class="quote-band__phone">0467 215 340</span>
    </div>
  </div>

  <footer class="web-bar">www.<strong>BrightFlowPlumbing</strong>.com.au</footer>
</main>
</body>
</html>
```